TIVARELCAP web-presence redisign

We would like to have our existing web-presence redesigned. Have a look at www.tivarel.ch (please use explorer). To the existing 11 pages we would add one more.

```html
<!DOCTYPE html>
<html lang="de">
<head>
<meta charset="utf-8">
<title>TIVARELCAP Zahnarztpraxis</title>
<link rel="stylesheet" href="https://fonts.googleapis.com/css2?family=Open+Sans:wght@400;600;700&family=Tinos:wght@400&display=swap">
<style>
  :root {
    --header-outer: #ffc11f;
    --header-inner: #ffba00;
    --header-rule: #ffa800;
    --hero-outer: #e6e6e6;
    --hero-inner: #e2e2e2;
    --nav-outer: #2d2d2d;
    --nav-inner: #151515;
    --nav-rule: #dcdcdc;
    --main-outer: #1d1a4a;
    --main-inner: #000032;
    --footer-outer: #1b1a29;
    --footer-inner: #05040f;
    --text-light: #ffffff;
    --text-soft: #e8e8ee;
    --divider: #1f1d55;
    --icon: #d0d0d0;
    --smile: #2e2219;
  }
  * { box-sizing: border-box; margin: 0; padding: 0; }
  html, body { width: 1200px; height: 1000px; overflow: hidden; }
  body { font-family: "Open Sans", Arial, sans-serif; color: var(--text-light); }
  .band { position: absolute; left: 0; width: 1200px; }
  .inner { position: absolute; left: 200px; width: 800px; top: 0; height: 100%; }

  .header { top: 0; height: 108px; background: var(--header-outer); border-bottom: 5px solid var(--header-rule); }
  .header .inner { background: var(--header-inner); }
  .brand { position: absolute; left: 20px; top: 30px; display: flex; align-items: center; gap: 12px; }
  .brand-dot { width: 36px; height: 36px; border-radius: 50%; background: #fff; }
  .brand-name { font-family: "Tinos", "Times New Roman", serif; font-size: 32px; color: #fff; letter-spacing: 1px; }

  .hero { top: 108px; height: 297px; background: var(--hero-outer); }
  .hero .inner { background: var(--hero-inner); }
  .hero-line1 { position: absolute; left: 50px; top: 84px; font-family: "Tinos", "Times New Roman", serif; font-size: 46px; color: #fff; text-shadow: 2px 2px 4px rgba(0,0,0,.35); }
  .hero-line2 { position: absolute; left: 162px; top: 128px; font-family: "Tinos", "Times New Roman", serif; font-size: 80px; color: var(--smile); text-shadow: 3px 3px 5px rgba(0,0,0,.3); }
  .hero-photo { position: absolute; left: 455px; top: 0; width: 320px; height: 297px;
    background: radial-gradient(ellipse at 50% 45%, #d9ab8e 0%, #a97a5b 40%, #6e4a33 65%, rgba(226,226,226,0) 72%); }

  .nav { top: 405px; height: 42px; background: var(--nav-outer); border-bottom: 5px solid var(--nav-rule); }
  .nav .inner { background: var(--nav-inner); }
  .nav ul { list-style: none; display: flex; justify-content: center; align-items: center; height: 37px; font-family: "Tinos", "Times New Roman", serif; font-size: 20px; color: #f2f2f2; }
  .nav li + li::before { content: "|"; margin: 0 20px; }

  .main { top: 447px; height: 416px; background: var(--main-outer); }
  .main .inner { background: var(--main-inner); padding: 0 20px; }
  .main h1 { font-size: 19px; font-weight: 700; margin-top: 33px; }
  .main p { font-size: 15px; line-height: 18px; color: var(--text-soft); margin-top: 17px; }
  .main .divider { border: 0; border-top: 1px solid var(--divider); margin: 32px 0 25px; }
  .social { position: absolute; left: 323px; top: 355px; display: flex; gap: 14px; }
  .social span { width: 42px; height: 42px; border-radius: 50%; background: var(--icon); }

  .footer { top: 863px; height: 137px; background: var(--footer-outer); }
  .footer .inner { background: var(--footer-inner); font-size: 15px; line-height: 18px; color: var(--text-soft); }
  .footer-legal { position: absolute; left: 19px; top: 24px; }
  .footer-contact { position: absolute; left: 628px; top: 24px; }
  .footer-contact p + p { margin-top: 18px; }
</style>
</head>
<body>
  <header class="band header">
    <div class="inner">
      <div class="brand"><span class="brand-dot"></span><span class="brand-name">TIVARELCAP</span></div>
    </div>
  </header>

  <section class="band hero">
    <div class="inner">
      <div class="hero-line1">Brighten your</div>
      <div class="hero-line2">SMILE!</div>
      <div class="hero-photo" role="img" aria-label="Portrait photo of a smiling young woman with long brown hair"></div>
    </div>
  </section>

  <nav class="band nav">
    <div class="inner">
      <ul><li>Home</li><li>Zahnmedizin</li><li>Dentalhygiene</li><li>Team</li><li>Kontakt</li></ul>
    </div>
  </nav>

  <main class="band main">
    <div class="inner">
      <h1>Herzlich willkommen in unserer neuen Praxis.</h1>
      <p>Es ist unser Ziel, Ihr Wohlbefinden zu steigern. Sie sollen die Schönheit des Alltags mit gesunden Zähnen geniessen und in jeder Situation herzhaft lachen können.</p>
      <p>Ihre Zahnärztin</p>
      <p>Dr. med. dent. Selina Marthaler-Kunz</p>
      <hr class="divider">
      <p>Learnt more about out dental practice, see out produsts and services and discover the different sections of this web site.</p>
      <p>Contact us to schedue a visit here</p>
      <div class="social" aria-label="Social media links"><span></span><span></span><span></span></div>
    </div>
  </main>

  <footer class="band footer">
    <div class="inner">
      <div class="footer-legal">Copyright 2007 © TIVARELCAP | Dr. med. dent. S. Marthaler-Kunz.<br>All rights reserved. Privacy Policy</div>
      <div class="footer-contact">
        <p>Lindenweg 12<br>CH-8604 Volketswil</p>
        <p>T: +41 (0)44 555 01 23<br>info@tivarel.ch</p>
      </div>
    </div>
  </footer>
</body>
</html>
```